Audio-Visual & Video Communications Business Requires a Cutting-edge Business Card Design

LinkHarbor is a new Audio-Visual & Video Communications company in Cape Town, South Africa that is looking for a cutting-edge business card design. We sell these products to the Corporate, Education & Hospitality markets and will also host an Online Shop for companies and individuals to purchase our products online.

We are already using the following two colours in our logo and draft website. Please incorporate these colours into the design. Please note that our website is still in the design stage if you need to visit it. Green #a0ce4e & Dark Grey #333333.
Updates

Hi,

Please note that I have uploaded our logo in an .eps format.

Target Market(s)

Corporate Companies, Education Institutions & Hospitality Markets

Industry/Entity Type

Business

Requirements
Nice to have
• It would be great if you could incorporate the services that we offer.

1. Consultation & Design
2. Project Management
3. Supply & Installation
4. Onsite Support Personal
5. Online Shop

```html
<!DOCTYPE html>
<html lang="en">
<head>
<meta charset="utf-8">
<title>LinkHarbor – Business Card</title>
<link rel="stylesheet" href="https://fonts.googleapis.com/css2?family=Arimo:wght@400&family=Open+Sans:wght@700&display=swap">
<style>
  :root {
    --page: #ffffff;
    --card-dark: #4a4a4a;
    --brand-green: #76b900;
    --paper: #ffffff;
    --service-grey: #b3b3b3;
    --ink-dark: #444444;
  }
  html, body {
    margin: 0;
    padding: 0;
    width: 1200px;
    height: 900px;
    overflow: hidden;
    background: var(--page);
  }
  .canvas {
    position: relative;
    width: 1200px;
    height: 900px;
  }
  .card {
    position: absolute;
    left: 387px;
    width: 469px;
    height: 286px;
    filter: drop-shadow(0 10px 14px rgba(0,0,0,0.28));
  }
  .card--front { top: 127px; }
  .card--back { top: 499px; }
  .card-bg { fill: var(--card-dark); }
  .card-green { fill: var(--brand-green); }
  .card-seal { fill: var(--paper); }
  .holder-name { font-family: "Arimo", Arial, sans-serif; font-size: 20px; fill: var(--brand-green); }
  .contact-line { font-family: "Arimo", Arial, sans-serif; font-size: 13px; fill: var(--paper); }
  .contact-email { font-family: "Arimo", Arial, sans-serif; font-size: 13px; fill: var(--brand-green); }
  .service-rule { stroke: var(--brand-green); stroke-width: 2; }
  .service-item { font-family: "Open Sans", Arial, sans-serif; font-weight: 700; font-size: 11.5px; fill: var(--service-grey); }
  .brand-dot { fill: var(--brand-green); }
  .brand-name { font-family: "Open Sans", Arial, sans-serif; font-weight: 700; font-size: 24px; fill: var(--ink-dark); }
  .brand-web { font-family: "Arimo", Arial, sans-serif; font-size: 15px; fill: var(--ink-dark); }
  .icon { fill: none; stroke: var(--paper); stroke-width: 1.2; }
</style>
</head>
<body>
<main class="canvas">

  <svg class="card card--front" viewBox="0 0 469 286" aria-label="Business card front">
    <defs>
      <clipPath id="front-shape"><rect width="469" height="286" rx="18"/></clipPath>
    </defs>
    <g clip-path="url(#front-shape)">
      <rect class="card-bg" width="469" height="286"/>
      <circle class="card-seal" cx="126" cy="233" r="128"/>
    </g>

    <text class="holder-name" x="23" y="42">Daniel Mercer</text>
    <text class="contact-email" x="446" y="40" text-anchor="end">me@linkharbor.co.za</text>
    <text class="contact-line" x="23" y="64">27 Kestrel Lane • Cape Town - South Africa</text>

    <g class="phone-mobile">
      <rect class="icon" x="25" y="71" width="7" height="12" rx="1"/>
      <line class="icon" x1="26.5" y1="80" x2="30.5" y2="80"/>
    </g>
    <text class="contact-line" x="37" y="84">+27 81 304-2219</text>
    <g class="phone-desk">
      <path class="icon" d="M156 80 h12 l-1.5 -4 h-9 z M157 76 q5 -5 10 0"/>
    </g>
    <text class="contact-line" x="176" y="84">+27 21 468-7350</text>

    <line class="service-rule" x1="290" y1="167" x2="469" y2="167"/>
    <text class="service-item" x="291" y="186">Consultation &amp; Design</text>
    <text class="service-item" x="291" y="207">Project Management</text>
    <text class="service-item" x="291" y="228">Supply &amp; Installation</text>
    <text class="service-item" x="291" y="249">Onsite Support Personal</text>
    <text class="service-item" x="291" y="270">Online Shop</text>

    <circle class="brand-dot" cx="123" cy="163" r="22"/>
    <text class="brand-name" x="123" y="235" text-anchor="middle">LinkHarbor</text>
    <text class="brand-web" x="123" y="272" text-anchor="middle">www.linkharbor.co.za</text>
  </svg>

  <svg class="card card--back" viewBox="0 0 469 286" aria-label="Business card back">
    <defs>
      <clipPath id="back-shape"><rect width="469" height="286" rx="18"/></clipPath>
    </defs>
    <g clip-path="url(#back-shape)">
      <rect class="card-bg" width="469" height="286"/>
      <polygon class="card-green" points="293,0 469,0 469,286 199,286"/>
      <circle class="card-seal" cx="235" cy="234" r="130"/>
    </g>
    <circle class="brand-dot" cx="233" cy="165" r="22"/>
    <text class="brand-name" x="233" y="235" text-anchor="middle">LinkHarbor</text>
    <text class="brand-web" x="233" y="272" text-anchor="middle">www.linkharbor.co.za</text>
  </svg>

</main>
</body>
</html>
```